Tallymint - A/B testing for professionals

We need to improve the presentation layer (design only) of our tool tallymint.example.

www.tallymint.example is a A/B testing tool for websites and all kind of applications. The most important features are already listed on our actual webpage and the attached screenshots.
the animated icons on the front page should be included into the design and should match the color scheme. if you think you need to add a logo or similar things to it - feel free to offer us good proposals. you can reach us by sending us a mail to: support@tallymint.example

our needs listed:
-we'd rather have a very good improvement of the actual design instead of a big redesign with all colours changed etc.
- the pages in the screenshots attached should be redesigned. The amount of different layouts will be around 2 - 4 depending on the design.
- the animated icons on www.tallyrmint.example must be included into the design.
- the colors should match with the animated icons.
- we won't need any code. Psd / ai / graphic files only.

Target Market(s)

everyone who sells something with their webpage / application.

Number of Pages Required

3 page

Colors
85cae6
3276b5
85abd2
cee9f5
eaf1f7
0455a3
000000
0492cd

Requirements
Must have
• - animated icons included on the main page.
• - color match with the animated icons on our website or good proposal for adjusting them accordingly.
• - touch of that is highly scaleable and adjustable: we invented a new query language for the project
• - sweetness of the modern web projects and libraries
• - touch that the date are not shared between different users - high value on privacy
Nice to have
• - proposal for a matching logo or including the actual properly
Should not have
• - images people in the design
• - coded versions

```html
<!DOCTYPE html>
<html lang="en">
<head>
<meta charset="utf-8">
<title>Tallymint – A/B Testing Made For Professionals</title>
<link href="https://fonts.googleapis.com/css2?family=Open+Sans:wght@300;400;600;700&display=swap" rel="stylesheet">
<style>
  :root{
    --brand-dark:#0455a3;
    --brand-mid:#3276b5;
    --brand-sky:#0492cd;
    --brand-light:#85cae6;
    --accent-yellow:#f5c623;
    --ink:#222;
    --ink-soft:#333;
    --card-bg:#f3f3f3;
    --contact-bg:#353535;
    --footer-bg:#2d2d2d;
    --white:#fff;
  }
  *{margin:0;padding:0;box-sizing:border-box}
  html,body{width:812px;height:1200px;overflow:hidden;background:var(--white)}
  body{position:relative;font-family:"Open Sans",Arial,sans-serif;color:var(--ink)}
  .abs{position:absolute}

  .hero{left:0;top:0;width:812px;height:484px;
    background:radial-gradient(ellipse at 50% 15%,#d6d6d8 0%,#a9aaae 35%,#6e6f73 70%,#4a4b4f 100%)}
  .brand{left:67px;top:15px;font-size:24px;font-weight:400;color:#e9e9e9;letter-spacing:.2px}
  .social{left:634px;top:15px;display:flex;gap:1px}
  .social span{width:26px;height:26px;border-radius:50%;background:var(--brand-dark);display:flex;align-items:center;justify-content:center}

  .nav{left:69px;top:61px;width:678px;height:41px;background:var(--white);display:flex;align-items:center}
  .nav a{font-size:11px;font-weight:600;color:var(--ink);text-decoration:none;padding:0 12px;height:41px;line-height:41px}
  .nav a.active{background:var(--brand-dark);color:var(--white);padding:0 13px}
  .nav .search{position:absolute;right:10px;top:11px}

  .slide{left:69px;top:134px;width:678px;height:296px;
    background:linear-gradient(180deg,#2aa7de 0%,#4db7e6 55%,#7cc9ec 100%)}
  .slide-title{left:0;width:678px;top:14px;text-align:center;font-size:22px;font-weight:400;color:var(--white)}
  .slide-title em{font-style:normal;color:var(--accent-yellow)}
  .slide-btn{left:290px;top:49px;width:98px;height:30px;background:var(--brand-dark);color:var(--white);font-size:10px;line-height:30px;text-align:center}
  .tool-shot{left:65px;top:89px;width:548px;height:207px;background:linear-gradient(90deg,#f7f7f7 0%,#eef3f7 100%);border:1px solid #cfd4d8}
  .tool-shot .tabs{height:22px;background:#e3e3e3;border-bottom:1px solid #cfcfcf}
  .tool-shot .split{position:absolute;left:275px;top:22px;bottom:0;width:1px;background:#cfcfcf}
  .tool-shot .sel{position:absolute;left:0;top:108px;width:265px;height:9px;background:#4aa3d8}

  .arrow{width:38px;height:28px;background:#555;display:flex;align-items:center;justify-content:center}
  .arrow.prev{left:54px;top:266px}
  .arrow.next{left:725px;top:266px}
  .dots{left:383px;top:447px;display:flex;gap:4px}
  .dots i{width:14px;height:14px;border-radius:50%;background:var(--white)}
  .dots i.on{background:#333}

  .section-title{left:0;width:812px;top:508px;text-align:center;font-size:24px;font-weight:400;color:var(--ink-soft)}
  .section-rule{left:365px;top:544px;width:83px;height:3px;background:var(--brand-dark)}

  .card{top:570px;width:221px;height:326px;background:var(--card-bg);border:1px solid #ececec}
  .card h3{position:absolute;left:22px;top:18px;font-size:17px;font-weight:400;color:var(--ink-soft);white-space:nowrap}
  .card .art{position:absolute;left:36px;top:52px;width:148px;height:112px;border-radius:50%/22% ;
    background:radial-gradient(ellipse at 50% 80%,#a9d6e6 0%,#bfe0ec 45%,rgba(243,243,243,0) 72%)}
  .card p{position:absolute;left:22px;width:185px;font-size:8.6px;line-height:9.6px;color:var(--ink)}
  .card p.a{top:174px}
  .card p.b{top:222px}
  .card .more{position:absolute;left:71px;top:272px;width:79px;height:25px;background:#2b2b2b;color:var(--white);font-size:9.5px;font-weight:700;line-height:25px;text-align:center}

  .divider{left:0;top:932px;width:812px;height:4px;background:#e2e2e2}
  .contact{left:0;top:936px;width:812px;height:216px;background:var(--contact-bg);color:var(--white);text-align:center}
  .contact h2{position:absolute;left:0;width:812px;top:22px;font-size:22px;font-weight:400}
  .contact .lede{position:absolute;left:130px;width:552px;top:64px;font-size:10.3px;line-height:13px}
  .contact .addr{position:absolute;left:0;width:812px;top:114px;font-size:10.5px}
  .contact .lines{position:absolute;left:0;width:812px;top:131px;font-size:10.5px;display:flex;justify-content:center;gap:49px}
  .contact .cta{position:absolute;left:330px;top:169px;width:150px;height:29px;background:var(--brand-dark);font-size:10.5px;line-height:29px}

  .footer{left:0;top:1152px;width:812px;height:48px;background:var(--footer-bg);border-top:3px solid #444}
  .footer .copy{position:absolute;left:66px;top:14px;font-size:9.5px;color:#ddd}
  .footer .icons{position:absolute;left:606px;top:10px;display:flex;gap:13px}
  .footer .icons span{width:24px;height:24px;display:flex;align-items:center;justify-content:center}
  .footer .icons .dot{width:16px;height:16px;border-radius:50%;background:#e8e8e8}
</style>
</head>
<body>

<header class="abs hero">
  <div class="abs brand">Tallymint</div>
  <div class="abs social">
    <span><svg width="13" height="10" viewBox="0 0 13 10"><rect x=".5" y=".5" width="12" height="9" fill="none" stroke="#fff"/><path d="M.5 .5l6 5 6-5" fill="none" stroke="#fff"/></svg></span>
    <span></span>
    <span></span>
    <span><svg width="8" height="13" viewBox="0 0 8 13"><rect x=".7" y=".7" width="6.6" height="11.6" rx="1" fill="none" stroke="#fff" stroke-width="1.4"/></svg></span>
  </div>

  <nav class="abs nav">
    <a class="active">HOME</a><a>ABOUT US</a><a>SERVICES</a><a>CONTACTS US</a>
    <svg class="search" width="20" height="20" viewBox="0 0 20 20"><circle cx="8" cy="8" r="6" fill="none" stroke="#eee" stroke-width="1.6"/><path d="M12.5 12.5l6 6" stroke="#eee" stroke-width="1.8"/></svg>
  </nav>

  <section class="abs slide">
    <h1 class="abs slide-title"><em>A/B</em> Testing Made For Professionals.</h1>
    <div class="abs slide-btn">Install &amp; Configure</div>
    <div class="abs tool-shot" role="img" aria-label="Screenshot of the Tallymint browser editor showing page elements and CSS rules">
      <div class="tabs"></div>
      <div class="split"></div>
      <div class="sel"></div>
    </div>
  </section>

  <div class="abs arrow prev"><svg width="10" height="14" viewBox="0 0 10 14"><path d="M8 1L2 7l6 6" fill="none" stroke="#fff" stroke-width="1.8"/></svg></div>
  <div class="abs arrow next"><svg width="10" height="14" viewBox="0 0 10 14"><path d="M2 1l6 6-6 6" fill="none" stroke="#fff" stroke-width="1.8"/></svg></div>
  <div class="abs dots"><i></i><i class="on"></i><i></i></div>
</header>

<h2 class="abs section-title">Our Services</h2>
<div class="abs section-rule"></div>

<article class="abs card" style="left:69px">
  <h3>Create experiments di...</h3>
  <div class="art" role="img" aria-label="Isometric illustration of a house on a round blue island"></div>
  <p class="a">Uenim ad minim veniam, quis nostrud laboris nisi utaliquip ex ea commodo consequat. Duisute irurdolor into reprehenderitin voluptate velit esse cillum.</p>
  <p class="b">Uenim ad minim veniam, quis nostrud laboris nisi utaliquip ex ea commodo consequat.</p>
  <div class="more">READ MORE</div>
</article>
<article class="abs card" style="left:298px">
  <h3>Check results with ava...</h3>
  <div class="art" role="img" aria-label="Isometric illustration of a large monitor showing a bar chart"></div>
  <p class="a">Uenim ad minim veniam, quis nostrud laboris nisi utaliquip ex ea commodo consequat. Duisute irurdolor into reprehenderitin voluptate velit esse cillum.</p>
  <p class="b">Uenim ad minim veniam, quis nostrud laboris nisi utaliquip ex ea commodo consequat.</p>
  <div class="more">READ MORE</div>
</article>
<article class="abs card" style="left:526px">
  <h3>Flexible analysis using ...</h3>
  <div class="art" role="img" aria-label="Isometric illustration of a small building on a round blue island"></div>
  <p class="a">Uenim ad minim veniam, quis nostrud laboris nisi utaliquip ex ea commodo consequat. Duisute irurdolor into reprehenderitin voluptate velit esse cillum.</p>
  <p class="b">Uenim ad minim veniam, quis nostrud laboris nisi utaliquip ex ea commodo consequat.</p>
  <div class="more">READ MORE</div>
</article>

<div class="abs divider"></div>
<section class="abs contact">
  <h2>Contact Me</h2>
  <p class="lede">Lorem ipsum dolor sit amet, consectetuer adipiscing elit. Praesent vestibulum m olestie lacus. Aenean nonummy hendrerit mauris. Phasellus porta. Fusce suscipit varius mi. Lorem ipsum dolor sit amet, consectetuer adipiscing elit. Praesent vestibulum molestie lacus. Morbi nunc odio, gravida at, cursus neca</p>
  <p class="addr">PO Box 412 Marlow NSW 2031.</p>
  <div class="lines"><span>Telephone: +02 5550 1842</span><span>E-mail: hello@tallymint.example</span></div>
  <div class="cta">DROP ME A MASSAGE</div>
</section>

<footer class="abs footer">
  <div class="copy">Copyright © 2015 - All Rights Reserved</div>
  <div class="icons">
    <span><svg width="18" height="13" viewBox="0 0 18 13"><rect x=".8" y=".8" width="16.4" height="11.4" fill="none" stroke="#eee" stroke-width="1.5"/><path d="M.8 .8l8.2 6.4 8.2-6.4" fill="none" stroke="#eee" stroke-width="1.5"/></svg></span>
    <span><i class="dot"></i></span>
    <span><i class="dot"></i></span>
    <span><svg width="11" height="18" viewBox="0 0 11 18"><rect x="1" y="1" width="9" height="16" rx="1.5" fill="none" stroke="#eee" stroke-width="1.8"/></svg></span>
  </div>
</footer>

</body>
</html>
```